Tour operator needs simple coded WordPress site (updated extra payment for coding and guaranteed)

[update 9/7/2015]
If you design a new logo and it gets accepted, even if we use another template with your logo you will get $50
[update 8/7/2015]
Update on questions about dual-language
For dual languages we are happy to set up a second site with the same designs in a second language.
For the design aspect just allow the user to switch between languages with an icon.
For the coding, a replica of the site on a second server will do (to save messing around with multiple language plugins) - we will populate it with Chinese text
[original post]
Simple coded WordPress site for tours
You can choose to design only or design and code ($340 design, $150 bonus for coding)
Open design brief - use your creativity
Will be in 2 languages (English and Chinese) but design needs only to be in one language
Winning design will be chosen only from home page, but the winner must make a second standard template page when chosen at no extra cost.
Must be responsive design
We only need homepage and standard template page design and coding, we will populate the pages
You can use design ideas from our pamphlet if you like - attached
Only a sample logo and colors on website and pamphlet - feel free to change as the current ones seem restrictive
Current website framework only to give an idea of the number of pages and basic menu structure (no need to use existing navigation style or any style at all for that matter, open brief)
http://brightwaterlearningtrips.com.au/
Target Market(s)
Chinese parents of kids 10-14 (the kids will take the tour)
Industry/Entity Type
Tour
Number of Pages Required
2 page
Look and feel
Each slider illustrates characteristics of the customer's brand and the style your logo design should communicate.

```html
<!DOCTYPE html>
<html lang="en">
<head>
<meta charset="utf-8">
<title>Brightwater Learning Trips</title>
<link href="https://fonts.googleapis.com/css2?family=Open+Sans:wght@400;600;700&display=swap" rel="stylesheet">
<style>
:root{
  --orange:#f2a21d;
  --green:#86b84a;
  --green-dark:#6e9c38;
  --text:#555;
  --muted:#888;
  --footer:#1e1e1e;
  --footer-bottom:#141414;
  --night:#0d1f45;
  --white:#fff;
}
*{margin:0;padding:0;box-sizing:border-box}
html,body{width:753px;height:1200px;overflow:hidden;background:var(--white)}
body{font-family:'Open Sans',Arial,sans-serif;color:var(--text);position:relative}
.site-header{position:absolute;top:0;left:0;width:753px;height:80px;background:var(--white)}
.brand{position:absolute;left:40px;top:12px;display:flex;align-items:center;gap:8px}
.brand-mark{width:22px;height:22px;background:var(--orange)}
.brand-name{font-size:14px;font-weight:700;color:var(--orange);line-height:1.1;width:120px;text-transform:uppercase}
.main-nav{position:absolute;right:40px;top:27px;display:flex;gap:26px;align-items:center;font-size:11px}
.main-nav a{color:#333;text-decoration:none}
.lang{display:flex;gap:5px}
.lang span{width:14px;height:9px;display:block}
.lang .en{background:#2b3f8f}.lang .zh{background:#d9302a}
.hero{position:absolute;top:80px;left:0;width:753px;height:295px;background:linear-gradient(180deg,#0a1838 0%,#1b3d7a 45%,#2a5b9e 70%,#0b1a33 100%)}
.hero-title{position:absolute;left:100px;top:163px;font-size:17px;font-weight:700;color:var(--orange);line-height:1.25;text-transform:uppercase;letter-spacing:.3px}
.welcome{position:absolute;top:380px;left:0;width:753px;text-align:center}
.welcome h1{font-size:20px;font-weight:700;color:var(--orange)}
.welcome p{font-size:9px;color:var(--muted);width:420px;margin:8px auto 0;line-height:1.5}
.btn{display:inline-block;background:var(--green);color:var(--white);font-size:9px;padding:5px 12px;border-radius:10px;text-decoration:none}
.welcome .btn{margin-top:10px}
.photo{position:absolute;border:4px solid var(--white);box-shadow:0 1px 4px rgba(0,0,0,.25)}
.photo-students{left:95px;top:500px;width:255px;height:182px;background:linear-gradient(135deg,#e9e1d6,#cbb9a2 60%,#f1ede6)}
.photo-beach{left:392px;top:787px;width:255px;height:210px;background:linear-gradient(180deg,#9fc9e0 0%,#cfe3ec 45%,#efe7d6 70%,#c4a584 100%)}
.step{width:32px;height:32px;border-radius:50%;border:2px solid var(--green);color:var(--green);font-size:10px;display:flex;align-items:center;justify-content:center;background:var(--white)}
.feature{position:absolute}
.feature h2{font-size:16px;font-weight:600;color:var(--green);margin:6px 0 6px}
.feature ul{list-style:none;font-size:9px;line-height:1.55;color:#444}
.feature li::before{content:"";display:inline-block;width:4px;height:4px;background:var(--green);border-radius:50%;margin-right:6px;vertical-align:middle}
.safety{left:395px;top:482px;width:300px}
.includes{left:100px;top:726px;width:260px}
.btn-a{position:absolute;left:95px;top:692px}
.btn-b{position:absolute;left:597px;top:983px}
.site-footer{position:absolute;top:1018px;left:0;width:753px;height:157px;background:var(--footer);color:#bbb}
.footer-col{position:absolute;top:18px;font-size:8px;line-height:1.8}
.footer-col h3{font-size:11px;font-weight:600;color:var(--white);margin-bottom:8px}
.footer-col a{color:#bbb;text-decoration:none;display:block}
.col-links{left:80px}.col-account{left:190px}.col-contact{left:305px;width:128px}.col-follow{left:575px}
.contact-email{font-size:7px;white-space:nowrap}
.map{position:absolute;left:445px;top:40px;width:95px;height:72px;background:linear-gradient(135deg,#e6e3dc,#cfd8c6)}
.social{display:flex;gap:5px}
.social span{width:16px;height:16px;display:block;background:#4a6fa5}
.social span:nth-child(2){background:#3a9fd6}
.social span:nth-child(3){background:#c9482b}
.social span:nth-child(4){background:#4c4c4c}
.social-badge{width:50px;height:22px;background:#2f5f9c;margin-top:8px}
.footer-bottom{position:absolute;top:1175px;left:0;width:753px;height:25px;background:var(--footer-bottom);color:#777;font-size:7px;text-align:center;line-height:25px}
.icon{vertical-align:middle;margin-right:3px}
</style>
</head>
<body>
<header class="site-header">
  <div class="brand"><span class="brand-mark"></span><span class="brand-name">Brightwater Learning Trips</span></div>
  <nav class="main-nav">
    <a href="#">Home</a><a href="#">About Us</a><a href="#">Tours</a><a href="#">Contact Us</a>
    <span class="lang"><span class="en"></span><span class="zh"></span></span>
  </nav>
</header>

<section class="hero" role="img" aria-label="Harbour bridge and city skyline at dusk">
  <p class="hero-title">Educational, safe, culturally<br>enlightening and fun.</p>
</section>

<section class="welcome">
  <h1>WELCOME TEXT</h1>
  <p>At Brightwater Learning Trips we are passionate about educational travel and opportunities for students to gain academic and cultural understanding of Australia.</p>
  <a class="btn" href="#">Read More</a>
</section>

<div class="photo photo-students" role="img" aria-label="Smiling student with classmates"></div>
<a class="btn btn-a" href="#">Read More</a>

<div class="feature safety">
  <div class="step">01</div>
  <h2>Safety and security</h2>
  <ul>
    <li>Staff certified by the government for Working With Children</li>
    <li>Staff certified in first aid care</li>
    <li>Professional accommodation with excellent history in caring for children with extensively well documented</li>
    <li>Safety Management Procedures including:</li>
    <li>Safety Management – reducing risk when taking students out of the classroom</li>
    <li>Safety &amp; Emergency Procedures (Location specific)</li>
    <li>Standard Operating Procedures</li>
    <li>Activity Specific Risk Management Plans</li>
    <li>Area Assessment Documentation</li>
    <li>Medical Forms, Dietary Requirements Form (Visa ink)</li>
    <li>Incident &amp; Management Forms</li>
    <li>Clothing &amp; Equipment List</li>
  </ul>
</div>

<div class="feature includes">
  <div class="step">02</div>
  <h2>Includes</h2>
  <ul>
    <li>Return tickets</li>
    <li>Visa fees</li>
    <li>Travel accident insurance</li>
    <li>Accommodation</li>
    <li>Meals (breakfast, lunch and dinner)</li>
    <li>Transportation</li>
    <li>Courses and Lectures</li>
    <li>Guides</li>
    <li>Entry tickets and travel expenses</li>
  </ul>
</div>

<div class="photo photo-beach" role="img" aria-label="Kangaroo on a sunny beach"></div>
<a class="btn btn-b" href="#">Read More</a>

<footer class="site-footer">
  <div class="footer-col col-links"><h3>Quick Links</h3><a href="#">Home</a><a href="#">About Us</a><a href="#">Tour</a><a href="#">Contact Us</a></div>
  <div class="footer-col col-account"><h3>My Account</h3><a href="#">Login</a><a href="#">Sign Up</a><a href="#">Privacy</a><a href="#">Terms &amp; Conditions</a></div>
  <div class="footer-col col-contact">
    <h3><svg class="icon" width="8" height="10" viewBox="0 0 8 10"><path d="M4 0a4 4 0 0 0-4 4c0 3 4 6 4 6s4-3 4-6a4 4 0 0 0-4-4z" fill="#bbb"/></svg>Contact Us</h3>
    <span>24 Harbour Lane Unit 5</span><br>
    <span>Sunport NSW</span><br>
    <span>T: 02 5550 1234</span><br>
    <span class="contact-email">hello@brightwaterlearningtrips.com.au</span>
  </div>
  <div class="map" role="img" aria-label="Street map of office location"></div>
  <div class="footer-col col-follow">
    <h3>Follow Us</h3>
    <div class="social"><span></span><span></span><span></span><span></span></div>
    <div class="social-badge"></div>
  </div>
</footer>
<div class="footer-bottom">© 2015 Brightwater Learning Trips | All Rights Reserved</div>
</body>
</html>
```